Triple Pane Vanity Makeup Mirrors Packaging

We need a box design for a triple pane vanity we are selling for Corvid Bargains. Corvid logo is attached. There will need to be an area for a UPC code(code will be uploaded this week)

An Overview / Background of the Business & Services
-Corvid Bargains/Corvid Outlet is an online seller on the Brellix
marketplace(Canada and US). We sell a variety of products from
video games to home goods(fans, mirrors, lamps, oil diffusers, etc).

The Target Market / Audience you are trying to reach
-Mainly women who take their makeup preparation and application seriously.

Design Specifics; any preferences or ideas for Style, Colour, Imagery,
etc
-Please keep the design very feminine, classy, and professional.
- Include the company's logo on the design and use colors similar to
the logo(ie: red, orange, yellow) although tasteful use of other colors
will be considered.

Here are links to the products:

This mirror will be in white
https://www.tradevorn.example/product-detail/Tri-folding-fantastic-vanity-with-led_48190372615.html?spm=b3811.9552419.0.0.K28pt4

This mirror will be in black. It's dimensions are 32cm *20.5cm*10cm
https://www.tradevorn.example/product-detail/Customized-Tri-folding-make-up-led_2973048611.html?spm=b3811.9552419.0.0.K28pt4

The product description has been updated with links to the product.

Target Market(s)

Makeup and hair enthusiasts that want to take their preparation to the next level. These people use makeup and hair as an art, and the product will reflect that.

Industry/Entity Type

Hair And Beauty

Font styles to use
Decorative
Script

Colors

Designer to choose colors to be used in the design.

Requirements
Must have
• -Company logo
• -Spot for UPC code
Nice to have
• -this is our first packaging project and are very open to all ideas and designs.

```html
<!DOCTYPE html>
<html lang="en">
<head>
<meta charset="utf-8">
<title>Corvid – A Triple Pane Vanity Packaging</title>
<link href="https://fonts.googleapis.com/css2?family=Montserrat:wght@300;500;600&display=swap" rel="stylesheet">
<style>
  :root {
    --backdrop: #86aeb8;
    --box-black: #141416;
    --box-black-edge: #26262a;
    --brand-red: #c41d2f;
    --brand-red-deep: #a8172a;
    --wordmark: #6a6a5c;
    --title-white: #f2f2f2;
    --icon-white: #ffffff;
    --mirror-light: #eceff2;
    --mirror-skin: #e3c3b3;
    --upc-panel: #ffffff;
  }
  * { margin: 0; padding: 0; box-sizing: border-box; }
  html, body { width: 1200px; height: 1200px; overflow: hidden; }
  body {
    background: var(--backdrop);
    font-family: "Montserrat", sans-serif;
    position: relative;
  }
  .box-front {
    position: absolute;
    left: 220px; top: 80px;
    width: 760px; height: 1040px;
    background: linear-gradient(160deg, var(--box-black-edge) 0%, var(--box-black) 45%);
    overflow: hidden;
  }
  .feature-band {
    position: absolute;
    left: 0; bottom: 0;
    width: 100%; height: 400px;
    background: radial-gradient(ellipse at 55% 25%, var(--brand-red) 0%, var(--brand-red-deep) 100%);
  }
  .brand-logo {
    position: absolute;
    top: 120px; left: 0;
    width: 100%;
    display: flex;
    justify-content: center;
    align-items: center;
    gap: 18px;
  }
  .brand-dot {
    width: 34px; height: 34px;
    border-radius: 50%;
    background: var(--brand-red);
  }
  .wordmark {
    font-size: 66px;
    font-weight: 500;
    line-height: 1;
    color: var(--wordmark);
    letter-spacing: 2px;
  }
  .product-title {
    position: absolute;
    top: 235px; width: 100%;
    text-align: center;
    font-size: 54px;
    font-weight: 300;
    line-height: 1.1;
    color: var(--title-white);
    letter-spacing: 1px;
  }
  .product-photo {
    position: absolute;
    left: 40px; top: 345px;
    width: 680px; height: 470px;
    background: linear-gradient(180deg, var(--mirror-light) 0%, var(--mirror-skin) 55%, var(--mirror-light) 100%);
  }
  .magnify-label {
    position: absolute;
    left: 10px;
    font-size: 22px;
    font-weight: 600;
    color: #222;
  }
  .magnify-label.two-x { top: 185px; }
  .magnify-label.three-x { top: 415px; }
  .feature-list {
    position: absolute;
    left: 30px; right: 200px; bottom: 70px;
    display: flex;
    justify-content: space-around;
    list-style: none;
  }
  .feature {
    display: flex;
    flex-direction: column;
    align-items: center;
    gap: 10px;
    width: 120px;
  }
  .feature-icon { width: 58px; height: 58px; }
  .feature-label {
    font-size: 12px;
    font-weight: 500;
    color: var(--icon-white);
    text-align: center;
    white-space: nowrap;
  }
  .upc-spot {
    position: absolute;
    right: 40px; bottom: 50px;
    width: 150px; height: 100px;
    background: var(--upc-panel);
    border-radius: 4px;
  }
</style>
</head>
<body>
  <main class="box-front">
    <div class="feature-band"></div>

    <div class="brand-logo">
      <span class="brand-dot"></span>
      <span class="wordmark">Corvid</span>
    </div>
    <h1 class="product-title">A Triple Pane Vanity</h1>

    <div class="product-photo" role="img" aria-label="Photo of the white tri-fold LED vanity mirror on its round stand, with close-up magnified reflections in the side panes">
      <span class="magnify-label two-x">2X</span>
      <span class="magnify-label three-x">3X</span>
    </div>

    <ul class="feature-list">
      <li class="feature">
        <svg class="feature-icon" viewBox="0 0 58 58" fill="none" stroke="var(--icon-white)" stroke-width="2.5">
          <circle cx="29" cy="29" r="26"/>
          <path d="M17 27a12 12 0 0 1 22-6"/><path d="M39 15v6h-6"/>
          <path d="M41 31a12 12 0 0 1-22 6"/><path d="M19 43v-6h6"/>
        </svg>
        <span class="feature-label">Rotation</span>
      </li>
      <li class="feature">
        <svg class="feature-icon" viewBox="0 0 58 58" fill="none" stroke="var(--icon-white)" stroke-width="2.5">
          <circle cx="29" cy="29" r="26"/>
          <rect x="22" y="16" width="14" height="28" rx="2"/>
          <rect x="26" y="13" width="6" height="3" fill="var(--icon-white)"/>
          <rect x="25" y="32" width="8" height="9" fill="var(--icon-white)" stroke="none"/>
        </svg>
        <span class="feature-label">Battery Usage</span>
      </li>
      <li class="feature">
        <svg class="feature-icon" viewBox="0 0 58 58" fill="none" stroke="var(--icon-white)" stroke-width="2.5" stroke-linecap="round">
          <circle cx="29" cy="29" r="26"/>
          <path d="M21 20a13 13 0 1 0 16 0"/><path d="M29 15v14"/>
        </svg>
        <span class="feature-label">Touch Switch</span>
      </li>
      <li class="feature">
        <svg class="feature-icon" viewBox="0 0 58 58" fill="none" stroke="var(--icon-white)" stroke-width="2.5">
          <circle cx="29" cy="29" r="26"/>
          <rect x="23" y="14" width="12" height="12" rx="1"/>
          <path d="M24 26v8h10v-8"/><path d="M29 34v10"/>
        </svg>
        <span class="feature-label">USB Charge</span>
      </li>
    </ul>

    <div class="upc-spot" role="img" aria-label="Reserved space for the UPC code"></div>
  </main>
</body>
</html>
```